KWB needs a professional PP

We are looking for a more professional powerpoint presentation that will be presented to prospective clients. This powerpoint needs to summarize all the services and value that The Harbinger Collective has to offer, pretty much giving an overview of the company.

The clients we deal with are Funeral Homes and Funeral Directors, we are an organization dedicated to assisting funeral homes in implementing highly profitable insurance programs while providing the training, support and service along the way. More information is provided in the brochure attached.

We are going for a professional simple theme, we want to get the message across without overwhelming the client.

I have attached our current powerpoint presentation as reference and more information about the our company and what we offer. This one is obviously what we are looking to replace, but the information will be generally the same. It needs to be more visually appealing and convey professionalism.

```html
<!DOCTYPE html>
<html lang="en">
<head>
<meta charset="utf-8">
<title>The Harbinger Collective – Presentation</title>
<link rel="stylesheet" href="https://fonts.googleapis.com/css2?family=Tinos:ital,wght@0,400;0,700;1,400&family=Cormorant+Garamond:wght@600&display=swap">
<style>
:root{
  --stage:#000;
  --navy:#0b4d9c;
  --navy-soft:#4f79b4;
  --title:#2a4a7f;
  --slate:#4b6a95;
  --ink:#111;
  --paper:#f1f1f2;
  --slide-top:#d9dadd;
  --slide-mid:#eeeff1;
  --footer:#ebebec;
  --callout:#dfe9f5;
  --table-head:#95b3dc;
  --table-row:#dce6f3;
  --table-alt:#eef3fa;
  --page-num:#c0793a;
}
*{box-sizing:border-box;margin:0;padding:0}
html,body{width:1200px;height:906px;overflow:hidden;background:var(--stage)}
body{font-family:"Tinos",serif;color:var(--ink)}
.deck{position:relative;width:1200px;height:906px}
.slide{position:absolute;width:555px;height:414px;overflow:hidden;
  background:linear-gradient(160deg,var(--slide-top) 0%,var(--slide-mid) 45%,var(--slide-top) 100%)}
.s1{left:25px;top:25px}.s2{left:618px;top:25px}.s3{left:25px;top:464px}.s4{left:618px;top:464px}

/* title slide */
.cover-band{position:absolute;left:0;right:0;top:118px;height:177px;background:var(--paper);box-shadow:0 2px 8px rgba(0,0,0,.25)}
.cover-rule{position:absolute;left:91px;width:375px;height:9px;background:var(--navy)}
.cover-rule.top{top:109px}.cover-rule.bottom{top:295px}
.brand-name{position:absolute;left:0;right:0;top:166px;text-align:center;font-size:35px;letter-spacing:-.5px;color:var(--slate);font-variant:small-caps}
.tagline{position:absolute;left:0;right:0;top:241px;text-align:center;font-size:15px;color:var(--slate)}

/* content slide chrome */
.topbar{position:absolute;left:0;top:0;width:100%;height:10px;background:var(--navy)}
.topbar span{position:absolute;top:0;height:10px;background:var(--navy-soft)}
.slide-title{position:absolute;left:18px;top:22px;font-family:"Cormorant Garamond",serif;font-weight:600;font-variant:small-caps;font-size:30px;color:var(--title);letter-spacing:.5px;text-shadow:1px 1px 1px rgba(0,0,0,.2)}
.footer{position:absolute;left:0;bottom:0;width:100%;height:38px;background:var(--footer)}
.footer-name{position:absolute;left:22px;top:12px;font-size:13px;color:var(--slate);font-variant:small-caps;letter-spacing:-.3px}
.page-num{position:absolute;right:30px;top:13px;font-size:9px;color:var(--page-num)}

/* about slide */
.points{position:absolute;left:30px;top:74px;width:500px;list-style:none;font-size:17.5px;line-height:1.3}
.points>li{position:relative;padding-left:20px;margin-bottom:7px}
.points>li::before{content:"";position:absolute;left:2px;top:8px;border-left:7px solid var(--navy-soft);border-top:4px solid transparent;border-bottom:4px solid transparent}
.points ul{list-style:none;margin-top:6px;font-size:12.5px;line-height:1.55}
.points ul li{position:relative;padding-left:16px}
.points ul li::before{content:"–";position:absolute;left:0}
.callout{position:absolute;left:258px;top:282px;width:297px;height:98px}
.callout-text{position:absolute;left:312px;top:301px;width:220px;font-style:italic;font-size:12.5px;color:var(--navy-soft);line-height:1.35}
.callout-text span{display:block}

/* rate slide */
.rates{position:absolute;left:44px;top:89px;width:460px;border-collapse:collapse;font-size:7.5px;text-align:center}
.rates th{background:var(--table-head);font-size:11.5px;font-weight:700;padding:2px 3px;line-height:1.05;border:1px solid #fff}
.rates td{padding:2px 3px;border:1px solid #fff;background:var(--table-row)}
.rates tr:nth-child(even) td{background:var(--table-alt)}
.rates-shadow{position:absolute;left:38px;top:83px;width:472px;height:108px;background:rgba(255,255,255,.6);box-shadow:0 2px 6px rgba(0,0,0,.3)}
.note{position:absolute;left:38px;top:218px;width:472px;height:138px;background:var(--paper);box-shadow:0 3px 8px rgba(0,0,0,.3);text-align:center;font-size:12.5px;line-height:1.35;padding:18px 20px}
.note p+p{margin-top:14px}

/* partners slide */
.partner-card{position:absolute;left:185px;width:323px;height:112px;background:var(--paper);box-shadow:0 3px 7px rgba(0,0,0,.25)}
.partner-badge{position:absolute;left:63px;width:130px;height:130px;border:6px solid var(--navy);border-radius:50% 6px 50% 50%;background:#fff;display:flex;align-items:center;justify-content:center;box-shadow:0 2px 6px rgba(0,0,0,.3)}
.partner-name{font-size:18px;font-weight:700;color:var(--navy)}
.partner-points{position:absolute;left:30px;top:30px;list-style:none;font-size:12.5px;line-height:1.35}
.partner-points li{position:relative;padding-left:14px}
.partner-points li::before{content:"";position:absolute;left:0;top:5px;border-left:5px solid var(--navy-soft);border-top:3px solid transparent;border-bottom:3px solid transparent}
</style>
</head>
<body>
<main class="deck">

  <section class="slide s1">
    <div class="cover-band"></div>
    <div class="cover-rule top"></div>
    <div class="cover-rule bottom"></div>
    <h1 class="brand-name">The Harbinger Collective</h1>
    <p class="tagline">Achieve More</p>
  </section>

  <section class="slide s2">
    <div class="topbar"><span style="left:48px;width:62px"></span><span style="left:110px;width:48px;opacity:.7"></span></div>
    <h2 class="slide-title">About The Harbinger Collective</h2>
    <ul class="points">
      <li>Nationwide (Pre-Planning) Consulting Firm</li>
      <li>Partner exclusively with Funeral Directors</li>
      <li>Provide Free, Professional Consulting for Funeral Home’s Pre-Planning Services</li>
      <li>Goals:
        <ul>
          <li>Assist in increasing your customer base and maximizing your revenue streams</li>
          <li>Work to provide you with more affordable pre-planning options to offer your customers</li>
        </ul>
      </li>
    </ul>
    <svg class="callout" viewBox="0 0 297 98" aria-hidden="true">
      <polygon points="40,8 297,8 297,90 40,90 0,49" fill="var(--callout)"/>
      <rect x="160" y="0" width="137" height="7" fill="var(--navy)"/>
      <rect x="160" y="91" width="137" height="7" fill="var(--navy)"/>
    </svg>
    <p class="callout-text"><span>Become more profitable.</span><span style="padding-left:76px">More successful.</span><span style="padding-left:128px">More secure.</span></p>
    <footer class="footer"><span class="footer-name">The Harbinger Collective</span><span class="page-num">2</span></footer>
  </section>

  <section class="slide s3">
    <div class="topbar"><span style="left:48px;width:62px"></span><span style="left:110px;width:48px;opacity:.7"></span></div>
    <h2 class="slide-title">Rate Chart Comparison</h2>
    <div class="rates-shadow"></div>
    <table class="rates">
      <tr><th>Age</th><th>Face Value</th><th>Pre Need Male</th><th>Final Expense Male</th><th>Pre Need Female</th><th>Final Expense Female</th></tr>
      <tr><td>65</td><td>$10,000.00</td><td>$230.00</td><td>$53.29</td><td>$230.00</td><td>$41.54</td></tr>
      <tr><td>70</td><td>$10,000.00</td><td>$247.50</td><td>$68.48</td><td>$247.50</td><td>$52.17</td></tr>
      <tr><td>75</td><td>$10,000.00</td><td>$275.00</td><td>$93.43</td><td>$275.00</td><td>$71.49</td></tr>
      <tr><td>80</td><td>$10,000.00</td><td>$422.59</td><td>$145.96</td><td>$422.59</td><td>$103.55</td></tr>
    </table>
    <div class="note">
      <p>If Pre-Need monthly payments are too expensive for your customers, chances are they will leave to consider other options <strong>without</strong> pre-planning through your funeral home.</p>
      <p>Let us help you keep the revenues in house and offer your customers more affordable Final Expense Options.</p>
    </div>
    <footer class="footer"><span class="footer-name">The Harbinger Collective</span><span class="page-num">10</span></footer>
  </section>

  <section class="slide s4">
    <div class="topbar"><span style="left:48px;width:62px"></span><span style="left:110px;width:48px;opacity:.7"></span></div>
    <h2 class="slide-title">Partners</h2>
    <div class="partner-card" style="top:90px">
      <ul class="partner-points"><li>Instant Approval</li><li>Competitively Low Rates</li></ul>
    </div>
    <div class="partner-badge" style="top:81px"><span class="partner-name">Bramwell Life</span></div>
    <div class="partner-card" style="top:235px">
      <ul class="partner-points" style="top:40px"><li>Relaxed Approval</li></ul>
    </div>
    <div class="partner-badge" style="top:226px"><span class="partner-name">Keystone Life</span></div>
    <footer class="footer"><span class="footer-name">The Harbinger Collective</span><span class="page-num">11</span></footer>
  </section>

</main>
</body>
</html>
```